GHalvor Busisness Card

I am an aerospace consultant and at this time only need business cards.

Industry/Entity Type

Business

Contact Information for Business Card

Halvorsen Associates,LLC
Marcus D. Halvorsen

348 Birch Meadow Drive
Hartwell AL 35612

256-555-0187 (cell)
256-555-0142 (fax)

marcushalvorsen@mailbrook.test

```html
<!DOCTYPE html>
<html lang="en">
<head>
<meta charset="utf-8">
<title>Halvorsen Associates, LLC — Business Card</title>
<link rel="stylesheet" href="https://fonts.googleapis.com/css2?family=Audiowide&family=Michroma&family=Aldrich&display=swap">
<style>
  :root {
    --page-bg: #e4e5e7;
    --card-bg: #3b3b3c;
    --card-edge: #2e2e2f;
    --ink-white: #f2f2f2;
    --ink-soft: #d9d9d9;
    --accent-green: #3fc23a;
    --glow-green: rgba(90, 220, 80, 0.55);
    --orbit-light: #5a5a5c;
  }
  * { box-sizing: border-box; margin: 0; padding: 0; }
  html, body {
    width: 1200px;
    height: 1000px;
    overflow: hidden;
    background: var(--page-bg);
  }
  .business-card {
    position: absolute;
    left: 100px;
    top: 215px;
    width: 1000px;
    height: 570px;
    background: var(--card-bg);
    border-radius: 6px;
    box-shadow: 0 10px 30px rgba(0, 0, 0, 0.25);
    overflow: hidden;
  }
  .orbit-artwork {
    position: absolute;
    right: 0;
    top: 0;
    width: 560px;
    height: 570px;
    background:
      radial-gradient(circle at 70% 58%, var(--glow-green) 0, rgba(90,220,80,0) 9%),
      radial-gradient(circle at 30% 40%, rgba(90,220,80,0.4) 0, rgba(90,220,80,0) 7%),
      radial-gradient(ellipse at 65% 55%, var(--orbit-light) 0%, var(--card-bg) 70%);
  }
  .company-name {
    position: absolute;
    left: 70px;
    top: 48px;
    font-family: "Michroma", sans-serif;
    font-size: 30px;
    letter-spacing: 3px;
    color: var(--ink-white);
    text-transform: uppercase;
  }
  .company-rule {
    position: absolute;
    left: 62px;
    top: 96px;
    width: 560px;
    height: 4px;
    background: var(--accent-green);
  }
  .person-name {
    position: absolute;
    left: 70px;
    top: 140px;
    padding: 14px 22px;
    font-family: "Audiowide", sans-serif;
    font-size: 44px;
    letter-spacing: 3px;
    color: var(--accent-green);
    text-transform: uppercase;
  }
  .bracket {
    position: absolute;
    width: 22px;
    height: 100%;
    top: 0;
    border: 4px solid var(--ink-white);
  }
  .bracket-left { left: 0; border-right: none; }
  .bracket-right { right: 0; border-left: none; }
  .contact-block {
    position: absolute;
    left: 70px;
    font-family: "Aldrich", sans-serif;
    font-size: 25px;
    line-height: 38px;
    letter-spacing: 2px;
    color: var(--ink-soft);
    text-transform: uppercase;
  }
  .contact-phones { top: 258px; }
  .contact-address { top: 408px; }
  .guide-line {
    position: absolute;
    left: 60px;
    top: 520px;
    width: 420px;
    border-top: 2px dashed var(--ink-soft);
    opacity: 0.7;
  }
</style>
</head>
<body>
  <article class="business-card">
    <div class="orbit-artwork" role="img" aria-label="Decorative orbital diagram with circles, star points and glowing green dots"></div>

    <h1 class="company-name">Halvorsen Associates,LLC</h1>
    <div class="company-rule"></div>

    <h2 class="person-name">
      <span class="bracket bracket-left"></span>
      Marcus D. Halvorsen
      <span class="bracket bracket-right"></span>
    </h2>

    <p class="contact-block contact-phones">
      M: 256-555-0187<br>
      F: 256-555-0142<br>
      marcushalvorsen@mailbrook.test
    </p>

    <p class="contact-block contact-address">
      348 Birch Meadow Drive<br>
      Hartwell, AL 35612
    </p>

    <div class="guide-line"></div>
  </article>
</body>
</html>
```